Investment firm needs refreshed corporate powerpoint slides design

We need a new and refreshed powerpoint template for our corporate investment deck. We are a technology private equity group that primarily invests in fast growing software companies and we would like to reflect that in a modern and light blue / transparant / white powerpoint and fonts template. I have also attached our old investor deck as a guideline and also check out our website to get an idea of what we do and what type of companies we invested in. Please note that our website is old and so our presentation should be a refreshed "2017" modern design, not a copy / paste of our website design and graphics.
Updates

Project Deadline Extended Reason: I'm extending the deadline to February 27, but we would ideally receive something by the end of this week.Please submit updates. Thanks Added Tuesday, February 21, 2017

Target Market(s)

Investors such as high net worth individuals, pension funds, banks, financial advisors

Industry/Entity Type

Investment

Colors
33a6d7
85cae6
cfeae6
edf8f6
ffffff
fff3d1
86cfc6

Requirements
Must have
• We let you be creative, we trust you have seen more investment presentations before.
Nice to have
• Pre-built models, flow charts, graphs, charts, etc.
Should not have
• Fancy or edgy images, this has to be a modern, fresh and trustworthy looking powerpoint template. No stock images, if you do use stock images for background purposes please be creative! :-)

```html
<!DOCTYPE html>
<html lang="en">
<head>
<meta charset="utf-8">
<title>HV Growth Equity – Deck Template</title>
<link href="https://fonts.googleapis.com/css2?family=Arimo:ital,wght@0,400;0,700;1,400&display=swap" rel="stylesheet">
<style>
  :root {
    --canvas: #d1d3d4;
    --navy: #163864;
    --teal: #2ebfd0;
    --pale-teal: #eaf6f9;
    --row-blue: #a5dde6;
    --grey-band: #b3b3b3;
    --subtitle-grey: #a7a9ac;
    --white: #ffffff;
  }
  html, body {
    margin: 0;
    padding: 0;
    width: 1200px;
    height: 1200px;
    overflow: hidden;
    background: var(--canvas);
    font-family: "Arimo", Arial, sans-serif;
  }
  .slide {
    position: absolute;
    left: 312px;
    width: 576px;
    height: 432px;
    background: var(--white);
    overflow: hidden;
  }
  .slide--title { top: 126px; }
  .slide--agenda { top: 642px; }
  .shape { position: absolute; left: 0; top: 0; }

  .hero-band {
    position: absolute; left: 0; top: 0;
    width: 576px; height: 144px;
    background: var(--teal);
  }
  .hero-art {
    position: absolute; left: 132px; top: 0;
    width: 300px; height: 144px;
    background: linear-gradient(90deg, var(--teal), #39b3c8 50%, var(--teal));
  }
  .deck-title {
    position: absolute; left: 143px; top: 203px;
    margin: 0; font-size: 35px; font-weight: 700; color: var(--navy);
    letter-spacing: 0.2px; white-space: nowrap;
  }
  .deck-subtitle {
    position: absolute; left: 143px; top: 272px;
    margin: 0; font-size: 19px; color: var(--subtitle-grey); white-space: nowrap;
  }
  .subtitle-rule {
    position: absolute; left: 143px; top: 297px;
    width: 99px; height: 3px; background: var(--teal);
  }
  .deck-audience {
    position: absolute; left: 143px; top: 303px;
    margin: 0; font-size: 16px; font-style: italic; color: var(--navy);
  }
  .footer-bar {
    position: absolute; top: 389px; left: 0;
    width: 473px; height: 14px; background: var(--grey-band);
  }
  .footer-bar--short { left: 31px; width: 442px; top: 403px; }
  .footer-stub { position: absolute; left: 0; top: 403px; width: 14px; height: 14px; background: var(--grey-band); }
  .footer-date {
    position: absolute; left: 29px; top: 390px;
    font-size: 10px; color: var(--white); line-height: 12px;
  }
  .brand {
    position: absolute; left: 478px;
    display: flex; align-items: center; gap: 4px;
    font-size: 19px; color: var(--navy); line-height: 1;
  }
  .brand-mark {
    width: 6px; height: 6px; background: var(--grey-band);
  }
  .slide--title .brand { top: 386px; }
  .slide--agenda .brand { top: 400px; }

  .agenda-header {
    position: absolute; left: 0; top: 0;
    width: 576px; height: 72px; background: var(--grey-band);
  }
  .agenda-title {
    position: absolute; left: 86px; top: 20px;
    margin: 0; font-size: 26px; font-weight: 400; color: var(--navy);
  }
  .agenda-row {
    position: absolute; left: 0; width: 576px; height: 29px;
    background: var(--row-blue);
  }
  .agenda-icon { position: absolute; left: 68px; top: 5px; }
  .agenda-label {
    position: absolute; left: 126px; top: 7px;
    font-size: 13px; color: var(--navy); white-space: nowrap;
  }
  .agenda-sublist {
    position: absolute; left: 138px; top: 166px;
    margin: 0; padding: 0; list-style: none;
    font-size: 12.5px; color: var(--navy); line-height: 18px;
    white-space: nowrap;
  }
  .agenda-sublist li::before {
    content: ""; display: inline-block;
    border-left: 4px solid var(--navy);
    border-top: 3.5px solid transparent; border-bottom: 3.5px solid transparent;
    margin-right: 4px; vertical-align: 1px;
  }
</style>
</head>
<body>

<section class="slide slide--title">
  <div class="hero-band"></div>
  <div class="hero-art" role="img" aria-label="Illustration of business people walking while one rises away on a rocket"></div>
  <svg class="shape" width="576" height="432" aria-hidden="true">
    <polygon points="0,0 133,144 0,288" fill="var(--navy)"/>
    <polygon points="485,166 574,264 485,362" fill="var(--pale-teal)"/>
  </svg>
  <h1 class="deck-title">HV Growth Equity</h1>
  <p class="deck-subtitle">Introduction to Team and Track Record</p>
  <div class="subtitle-rule"></div>
  <p class="deck-audience">For US Investors</p>
  <div class="footer-bar"></div>
  <span class="footer-date">November 2016</span>
  <div class="brand"><span class="brand-mark"></span>Halvern</div>
</section>

<section class="slide slide--agenda">
  <div class="agenda-header"></div>
  <h2 class="agenda-title">Agenda</h2>

  <div class="agenda-row" style="top:100px">
    <svg class="agenda-icon" width="16" height="18" aria-hidden="true"><rect x="2" y="1" width="12" height="16" fill="none" stroke="#111" stroke-width="1.4"/><path d="M5 6h6M5 9h6M5 12h6" stroke="#111" stroke-width="1.2"/></svg>
    <span class="agenda-label">Executive Summary</span>
  </div>
  <div class="agenda-row" style="top:134px">
    <svg class="agenda-icon" width="18" height="18" aria-hidden="true"><circle cx="4" cy="4" r="3.3" fill="#111"/><circle cx="4" cy="13" r="3.3" fill="#111"/><circle cx="13" cy="13" r="3.3" fill="#111"/><polygon points="13,0 14.3,3 17.5,3.2 15,5.3 15.8,8.5 13,6.7 10.2,8.5 11,5.3 8.5,3.2 11.7,3" fill="#111"/></svg>
    <span class="agenda-label">Differentiated Model</span>
  </div>
  <ul class="agenda-sublist">
    <li>Team and Advisory Board</li>
    <li>Target Profile</li>
    <li>Proprietary Company and Executive Sourcing</li>
    <li>Operational Focus</li>
  </ul>
  <div class="agenda-row" style="top:244px">
    <svg class="agenda-icon" width="16" height="18" aria-hidden="true"><path d="M2 1h8l4 4v12H2z" fill="none" stroke="#111" stroke-width="1.3"/><path d="M5 8h6M5 11h6M5 14h6" stroke="#111" stroke-width="1.1"/></svg>
    <span class="agenda-label">Track Record</span>
  </div>
  <div class="agenda-row" style="top:278px">
    <svg class="agenda-icon" width="16" height="18" aria-hidden="true"><rect x="2" y="1" width="10" height="15" fill="none" stroke="#111" stroke-width="1.3"/><path d="M4 5h6M4 8h6M4 11h4" stroke="#111" stroke-width="1.1"/><path d="M9 16l5-5 1.5 1.5-5 5H9z" fill="#111"/></svg>
    <span class="agenda-label">Summary of Terms</span>
  </div>
  <div class="agenda-row" style="top:312px">
    <svg class="agenda-icon" width="18" height="20" aria-hidden="true"><path d="M2 1h8l4 4v12H2z" fill="none" stroke="#111" stroke-width="1.4"/><rect x="5" y="12" width="12" height="7" fill="none" stroke="#111" stroke-width="1.4"/></svg>
    <span class="agenda-label">Appendix</span>
  </div>

  <svg class="shape" width="576" height="432" aria-hidden="true">
    <polygon points="0,0 66,72 0,144" fill="var(--navy)"/>
    <g fill="var(--navy)">
      <polygon points="93,100 101,100 113,114.5 101,129 93,129 105,114.5"/>
      <polygon points="93,134 101,134 113,148.5 101,163 93,163 105,148.5"/>
      <polygon points="93,244 101,244 113,258.5 101,273 93,273 105,258.5"/>
      <polygon points="93,278 101,278 113,292.5 101,307 93,307 105,292.5"/>
      <polygon points="93,312 101,312 113,326.5 101,341 93,341 105,326.5"/>
    </g>
  </svg>

  <div class="footer-stub"></div>
  <div class="footer-bar footer-bar--short"></div>
  <div class="brand"><span class="brand-mark"></span>Halvern</div>
</section>

</body>
</html>
```